Ashcombe Heritage Guild Harvest Lantern Days Event Flyer - Historic Event

I need a flyer about the Ashcombe Heritage Guild's Harvest Lantern Days event October 8th and 9th. The centerpiece of Harvest Lantern Days is Civil War reenactments. I want the flyer to include the schedule of events and be eye catching on area bulletin boards. Our website is www.ashcombeheritageguild.org for more information and pictures. The website for the Calder Ridge Rangers reenactors is http://www.calderridgerangers.com/.

Target Market(s)

Our target market is middle ages (35-70) families and couples. Most are history buffs, especially about the Civil War.

Industry/Entity Type

Non-Profit

Font styles to use
Serif
Decorative
Script

Requirements
Must have
• The flyer must include the majority of the schedule attached - especially the battle times, museums, and anything including food.The dance on Saturday night is also important. The bottom of the flyer MUST say "Paid in part by Quillan County Visitor Levy Board"
Nice to have
• Pictures

```html
<!DOCTYPE html>
<html lang="en">
<head>
<meta charset="utf-8">
<title>Ashcombe Heritage Guild – Harvest Lantern Days</title>
<link rel="stylesheet" href="https://fonts.googleapis.com/css2?family=Rye&family=Smokum&family=Pinyon+Script&family=Crimson+Pro:ital,wght@0,400;0,600;0,700;1,400&family=Fira+Sans+Condensed:ital,wght@0,400;0,600;1,400&family=Open+Sans:wght@700&display=swap">
<style>
:root{
  --sky-top:#3e230e;
  --sky-mid:#c77a2a;
  --sky-glow:#e9a74a;
  --field:#8a6a2c;
  --field-dark:#4b3617;
  --gold:#f7e21c;
  --ink:#1b1410;
  --wine:#7b1f1c;
  --wine-dark:#6e1c18;
  --paper:#efe4e1;
  --paper-shade:#d9c6c2;
  --cream:#fbf3e6;
  --sepia:#8c6a5a;
}
*{box-sizing:border-box;margin:0;padding:0}
html,body{width:927px;height:1200px;overflow:hidden;background:var(--paper)}
.flyer{position:relative;width:927px;height:1200px;overflow:hidden;font-family:"Fira Sans Condensed",sans-serif;color:var(--ink)}

/* hero */
.hero{position:absolute;left:0;top:0;width:927px;height:456px;
  background:
    radial-gradient(ellipse 70% 30% at 50% 48%,rgba(240,175,80,.75),rgba(240,175,80,0) 70%),
    linear-gradient(180deg,var(--sky-top) 0%,#7a4419 18%,var(--sky-mid) 38%,var(--sky-glow) 47%,#9c6a2a 55%,var(--field) 72%,var(--field-dark) 100%);}
.hero-rule{position:absolute;left:0;top:452px;width:927px;height:7px;background:var(--wine-dark)}
.arc-title{position:absolute;left:0;top:0}
.place{position:absolute;top:104px;width:100%;text-align:center;font-family:"Pinyon Script",cursive;font-size:42px;line-height:1.2;color:var(--cream);-webkit-text-stroke:.6px #5a3a1a}
.event-title{position:absolute;top:172px;width:100%;text-align:center;white-space:nowrap;font-family:"Smokum","Rye",serif;font-weight:400;font-size:86px;line-height:1;color:var(--ink);letter-spacing:1px;text-shadow:0 0 2px #f3d9a8,0 0 6px rgba(255,230,180,.6)}
.event-sub{position:absolute;top:280px;width:100%;text-align:center;white-space:nowrap;font-family:"Rye",serif;font-weight:400;font-size:25px;line-height:1.2;letter-spacing:5px;color:var(--ink);text-shadow:0 0 3px #f1d29a}
.event-dates{position:absolute;top:371px;width:100%;text-align:center;font-family:"Open Sans",sans-serif;font-weight:700;font-size:27px;color:#fff}
.tagline{position:absolute;top:413px;width:100%;text-align:center;font-family:"Crimson Pro",serif;font-size:31px;color:var(--gold)}

/* schedule */
.schedule{position:absolute;left:0;top:459px;width:927px;height:463px;
  background:linear-gradient(180deg,#eadad7 0%,var(--paper) 40%,#f2e9e7 70%,var(--paper-shade) 100%)}
.day{position:absolute}
.day-sat{left:90px;top:0}
.day-sun{left:543px;top:0}
.day-title{position:absolute;left:0;white-space:nowrap;font-family:"Crimson Pro",serif;font-weight:700;font-size:21px;color:var(--wine)}
.note{position:absolute;left:0;white-space:nowrap;font-style:italic;font-size:14.5px}
.row{position:absolute;left:0;white-space:nowrap;font-size:15px;line-height:22px}
.row .time{position:absolute;left:0}
.row .time.soft{color:var(--wine)}
.row .what{position:absolute;left:103px;font-weight:600}
.row .what.battle{color:var(--wine)}
.row .detail{position:absolute;left:103px;top:22px;font-weight:400}
.row .detail.small{font-style:italic;font-size:14px}
.directions{position:absolute;left:0;top:290px;width:300px;font-family:"Crimson Pro",serif;font-size:18.5px;line-height:20px;color:var(--wine)}

.dance{position:absolute;left:110px;top:358px;width:290px;text-align:center;font-family:"Crimson Pro",serif}
.dance-time{font-weight:700;font-size:18px;margin-left:-40px}
.dance-title{font-weight:700;font-size:21px;line-height:22px;color:var(--wine);margin-top:4px}
.dance-sponsor{font-style:italic;font-size:20px;line-height:24px}
.dance-art{position:absolute;left:375px;top:346px;width:92px;height:116px;background:linear-gradient(180deg,#2a1d1a,#1b1410);border-radius:40px 40px 8px 8px;opacity:.85}

.contact{position:absolute;left:610px;top:398px;font-size:12px;line-height:18px}
.contact li{list-style:none;display:flex;align-items:center;gap:6px}
.contact svg{width:11px;height:11px;flex:none}

/* photos */
.photo{position:absolute;top:922px;height:213px}
.photo-tent{left:0;width:205px;background:linear-gradient(160deg,#d9c48a,#8a7a56 55%,#3d4a2a)}
.photo-cannon{left:205px;width:205px;background:linear-gradient(160deg,#b8978a,var(--sepia) 50%,#4e3a32)}
.photo-troop{left:410px;width:311px;background:linear-gradient(170deg,#c2a69a,#7d5f53 55%,#4a3830)}
.photo-cabin{left:721px;width:206px;background:linear-gradient(160deg,#7ea24a,#a78256 55%,#4a5a26)}
.photo-frame{position:absolute;inset:6px;border:3px solid #f6efe6}

.footer{position:absolute;left:0;top:1135px;width:927px;height:65px;background:var(--wine-dark);border-top:4px solid #f6efe6;
  display:flex;align-items:center;justify-content:center;font-family:"Crimson Pro",serif;font-size:22px;color:#fbeee0}
</style>
</head>
<body>
<main class="flyer">
  <div class="hero" role="img" aria-label="Photo of a battlefield at sunset with Civil War cannons in a golden field, trees and hills"></div>
  <div class="hero-rule"></div>

  <svg class="arc-title" width="927" height="160" viewBox="0 0 927 160" aria-label="Ashcombe Heritage Guild">
    <defs><path id="arc" d="M100 132 Q463 -18 832 132"/></defs>
    <text font-family="Rye, serif" font-size="46" fill="#f7e21c" stroke="#5a3a0a" stroke-width=".6" text-anchor="middle">
      <textPath href="#arc" startOffset="50%">Ashcombe Heritage Guild</textPath>
    </text>
  </svg>
  <p class="place">Ashcombe, Nebraska</p>
  <h1 class="event-title">HARVEST LANTERN DAYS</h1>
  <p class="event-sub">CIVIL WAR REENACTMENTS</p>
  <p class="event-dates">Saturday &amp; Sunday | October 8 &amp; 9, 2016</p>
  <p class="tagline">Come For a Weekend Full of History</p>

  <section class="schedule">
    <div class="day day-sat">
      <h2 class="day-title" style="top:22px">Saturday, October 8th, 2016</h2>
      <p class="note" style="top:55px">Through the Day | Demonstrations and Speakers in various locations</p>
      <div class="row" style="top:83px"><span class="time">10:00 AM</span><span class="what battle">Battle by Calder Ridge Rangers</span><span class="detail small">Sponsored in part by Hollis Corner Markets</span></div>
      <div class="row" style="top:135px"><span class="time">11:30-1:00</span><span class="what">Chicken Biscuit Bake</span><span class="detail">at Town Hall Free Will Donation</span></div>
      <div class="row" style="top:184px"><span class="time soft">Afternoon</span><span class="what">Trolley and Buggy Rides</span></div>
      <div class="row" style="top:214px"><span class="time">1:00-4:00</span><span class="what">Museums Opens</span></div>
      <div class="row" style="top:244px"><span class="time">1:30-2:00</span><span class="what">Birthday Cake on Everly House Front Porch</span><span class="detail small">Cake donated by Pennick Grocers, Marlow City</span></div>
      <div class="row" style="top:298px"><span class="time">2:00</span><span class="what battle">Battle by Calder Ridge Rangers</span></div>
      <div class="row" style="top:327px"><span class="time">3:00</span><span class="what">Sightseeing Cruise on the Spirit of Ashcombe</span></div>
    </div>

    <div class="dance">
      <p class="dance-time">6:00 PM</p>
      <p class="dance-title">Dance at Town Hall<br>with Lamplight Band</p>
      <p class="dance-sponsor">Sponsored by Dr. Whitlock</p>
    </div>
    <div class="dance-art" role="img" aria-label="Silhouette illustration of a couple dancing"></div>

    <div class="day day-sun">
      <h2 class="day-title" style="top:21px">Sunday, October 9th, 2016</h2>
      <div class="row" style="top:52px"><span class="time">12:30 PM</span><span class="what">Parade on Main Street</span></div>
      <div class="row" style="top:80px"><span class="time soft">Afternoon</span><span class="what">Buggy &amp; Trolley Rides</span></div>
      <div class="row" style="top:110px"><span class="time">1:00-4:00</span><span class="what">Museums Opens</span></div>
      <div class="row" style="top:139px"><span class="time">1:30</span><span class="what battle">Battle by Calder Ridge Rangers</span></div>
      <div class="row" style="top:170px"><span class="time">2:00</span><span class="what">Pie Reception</span><span class="detail">at Ashcombe Depot and</span><span class="detail" style="top:43px">&nbsp;Railroad History Museum</span></div>
      <div class="row" style="top:244px"><span class="time">3:00</span><span class="what">Sightseeing Cruise</span></div>
      <p class="directions">Ashcombe is on the Missouri River on US-212 west of Dell Harbor, MO</p>
    </div>

    <ul class="contact">
      <li><svg viewBox="0 0 12 12"><circle cx="6" cy="6" r="5" fill="none" stroke="#1b1410"/><ellipse cx="6" cy="6" rx="2.2" ry="5" fill="none" stroke="#1b1410"/><path d="M1 6h10" stroke="#1b1410"/></svg>www.ashcombeheritageguild.org</li>
      <li><svg viewBox="0 0 12 12"><path d="M1 5c0-2 2-3 5-3s5 1 5 3H8.5V4h-5v1zM2.5 6h7l1 4.5h-9z" fill="#1b1410"/></svg>(402) 555.0147</li>
      <li><svg viewBox="0 0 12 12"><rect x="1" y="2.5" width="10" height="7" fill="none" stroke="#1b1410"/><path d="M1 2.5l5 4 5-4" fill="none" stroke="#1b1410"/></svg>info@ashcombeheritageguild.org</li>
    </ul>
  </section>

  <div class="photo photo-tent" role="img" aria-label="Photo of a period canvas tent camp with reenactors, in an ornate frame"><span class="photo-frame"></span></div>
  <div class="photo photo-cannon" role="img" aria-label="Sepia photo of a reenactor firing a pistol beside a cannon"></div>
  <div class="photo photo-troop" role="img" aria-label="Sepia photo of a group of Civil War reenactors in uniform with rifles"></div>
  <div class="photo photo-cabin" role="img" aria-label="Photo of a historic log cabin among trees, in an ornate frame"><span class="photo-frame"></span></div>

  <footer class="footer">Paid in part by Quillan County Visitor Levy Board</footer>
</main>
</body>
</html>
```